Selvin: A Friday night in the Prophetic Flyer

We are holding 2 Friday night events, one on 10/25/19 and the other on 11/29/19.
The time frame is 6:30pm-9:00pm. These services will be a time of prayer/healing for the sick and will be prophetic as well. (There will be prophets prophesying over people)

The event is called: Selvin: A Friday night in the Prophetic
The flyer should also include the phrase/excerpt: "And they prophesied also".

Keywords/Phrases: Prophetic, Healing, Climbing in the Spirit, Higher level of Anointing...

Target Market(s)

those looking for healing, seeking a word from God

Colors

Designer to choose colors to be used in the design.

Requirements
Must have
• The event is called: Selvin: A Friday night in the Prophetic
• The flyer should also include the phrase/excerpt: "And they prophesied also".
• It must include the Tovik logo attached, either is fine, we have attached two different versions.
• It must have the dates, location, time
• Dates: October 25, 2019 and November 29, 2019
• Location: Hollard Community Center
• (Downtown Portland) 482 Wendle Street
• Portland, ME 04102
• Time: 6:30pm-9:00pm
• Contact Info: Tel. 207-555-3841
• email: contact@brimfield-hall.org
• web: www.tovik.org
Nice to have
• creativity in color scheme, the meaning of the word Selvin conveyed in a classy artistic way/design.
Should not have
• Crosses, pictures of churches

```html
<!DOCTYPE html>
<html lang="en">
<head>
<meta charset="utf-8">
<title>Selvin: A Friday Night in the Prophetic</title>
<link rel="stylesheet" href="https://fonts.googleapis.com/css2?family=Montserrat:wght@500;600;700;800&family=Kaushan+Script&display=swap">
<style>
  :root {
    --ink: #1b1b1b;
    --ink-deep: #141414;
    --orange: #f7931e;
    --white: #ffffff;
  }
  * { margin: 0; padding: 0; box-sizing: border-box; }
  html, body { width: 856px; height: 1200px; overflow: hidden; background: var(--ink); }
  .flyer {
    position: relative; width: 856px; height: 1200px; overflow: hidden;
    background: var(--ink);
    font-family: "Montserrat", sans-serif; color: var(--white);
  }
  .smoke { position: absolute; }
  .smoke--left-orange {
    left: -90px; top: 130px; width: 210px; height: 500px;
    background: radial-gradient(ellipse closest-side at 50% 50%, rgba(247,147,30,.9) 0%, rgba(247,147,30,.5) 45%, rgba(247,147,30,0) 100%);
  }
  .smoke--right-orange {
    right: -90px; top: 70px; width: 210px; height: 620px;
    background: radial-gradient(ellipse closest-side at 50% 50%, rgba(247,147,30,.9) 0%, rgba(247,147,30,.5) 45%, rgba(247,147,30,0) 100%);
  }
  .smoke--left-grey {
    left: -120px; top: 620px; width: 300px; height: 580px;
    background: radial-gradient(ellipse closest-side at 50% 50%, rgba(120,120,120,.5) 0%, rgba(120,120,120,.2) 50%, rgba(120,120,120,0) 100%);
  }
  .smoke--right-grey {
    right: -110px; top: 640px; width: 260px; height: 560px;
    background: radial-gradient(ellipse closest-side at 50% 50%, rgba(120,120,120,.45) 0%, rgba(120,120,120,.18) 50%, rgba(120,120,120,0) 100%);
  }
  .hands-photo {
    position: absolute; left: 90px; top: 300px; width: 690px; height: 440px;
    background: radial-gradient(ellipse closest-side at 50% 52%, rgba(110,110,110,.75) 0%, rgba(75,75,75,.55) 40%, rgba(45,45,45,.3) 70%, rgba(27,27,27,0) 100%);
  }
  .frame {
    position: absolute; left: 32px; top: 42px; width: 794px; height: 1142px;
    border: 5px solid var(--orange);
  }
  .frame__gap {
    position: absolute; left: 306px; top: 36px; width: 244px; height: 14px; background: var(--ink);
  }
  .event-series {
    position: absolute; top: 22px; left: 0; width: 856px; text-align: center;
    font-weight: 700; font-size: 54px; letter-spacing: 2px; color: var(--orange); line-height: 1;
  }
  .event-title {
    position: absolute; top: 84px; left: 0; width: 856px; text-align: center;
    font-weight: 800; font-size: 82px; line-height: 1; letter-spacing: 1px;
  }
  .event-subtitle {
    position: absolute; top: 160px; left: 0; width: 856px; text-align: center;
    font-family: "Kaushan Script", cursive; font-size: 66px; line-height: 1;
  }
  .date { position: absolute; top: 682px; text-align: center; line-height: 1; }
  .date--october { left: 138px; width: 190px; }
  .date--november { left: 530px; width: 200px; }
  .date__month { font-weight: 700; font-size: 33px; letter-spacing: -1px; }
  .date__day { margin-top: 8px; font-weight: 700; font-size: 44px; color: var(--orange); white-space: pre; }
  .scripture {
    position: absolute; left: 366px; top: 661px; width: 132px; height: 132px; border-radius: 50%;
    background: var(--ink-deep);
    display: flex; flex-direction: column; align-items: center; justify-content: center;
    color: var(--orange); font-weight: 800; line-height: 1; letter-spacing: -.5px;
  }
  .scripture__and { font-size: 34px; }
  .scripture__they { font-size: 22px; }
  .scripture__prophesied { font-size: 18px; margin: 2px 0; }
  .scripture__also { font-size: 23px; }
  .time {
    position: absolute; top: 813px; left: 0; width: 856px; text-align: center;
    font-weight: 700; font-size: 32px; line-height: 1;
  }
  .time__hour { color: var(--orange); }
  .venue {
    position: absolute; top: 858px; left: 0; width: 856px; text-align: center;
    font-weight: 600; font-size: 14px; letter-spacing: 1.2px; line-height: 1;
  }
  .venue__name { color: var(--orange); }
  .keywords {
    position: absolute; top: 894px; left: 0; width: 856px; text-align: center;
    font-weight: 700; font-size: 22px; letter-spacing: 2.4px; color: var(--orange); line-height: 1;
  }
  .keywords__sep { color: var(--white); }
  .tagline {
    position: absolute; top: 929px; left: 0; width: 856px; text-align: center;
    font-weight: 700; font-size: 30px; letter-spacing: 2.2px; line-height: 1;
  }
  .divider { position: absolute; left: 110px; top: 974px; width: 636px; height: 6px; }
  .contact {
    position: absolute; right: 112px; top: 1000px; text-align: right; line-height: 1;
  }
  .contact__lead { font-weight: 800; font-size: 20px; letter-spacing: 4.4px; }
  .contact__phone { margin-top: 14px; font-weight: 800; font-size: 34px; letter-spacing: 5px; color: var(--orange); }
  .contact__row { display: flex; justify-content: flex-end; align-items: center; gap: 12px; color: var(--orange); font-weight: 700; }
  .contact__row--email { margin-top: 10px; font-size: 17px; letter-spacing: 2.8px; }
  .contact__row--web { margin-top: 8px; font-size: 28px; letter-spacing: 4.4px; font-weight: 800; }
  .contact__icon { width: 30px; height: 22px; flex: none; }
  .contact__icon--globe { width: 28px; height: 28px; }
  .brand {
    position: absolute; left: 114px; top: 1058px; display: flex; align-items: center; gap: 8px;
  }
  .brand__dot { width: 14px; height: 14px; border-radius: 50%; background: var(--orange); }
  .brand__name { font-weight: 600; font-size: 38px; letter-spacing: 2px; color: var(--white); line-height: 1; }
</style>
</head>
<body>
<main class="flyer">
  <div class="smoke smoke--left-orange" role="img" aria-label="Orange smoke drifting along the left edge"></div>
  <div class="smoke smoke--right-orange" role="img" aria-label="Orange smoke and powder burst along the right edge"></div>
  <div class="smoke smoke--left-grey" role="img" aria-label="Grey smoke rising in the lower left"></div>
  <div class="smoke smoke--right-grey" role="img" aria-label="Grey smoke rising in the lower right"></div>
  <div class="hands-photo" role="img" aria-label="Black and white photograph of hands folded in prayer"></div>

  <div class="frame"></div>
  <div class="frame__gap"></div>

  <h1>
    <span class="event-series">SELVIN</span>
    <span class="event-title">A FRIDAY NIGHT</span>
    <span class="event-subtitle">in the Prophetic</span>
  </h1>

  <div class="date date--october">
    <div class="date__month">OCTOBER</div>
    <div class="date__day">2019. 25</div>
  </div>

  <div class="scripture">
    <span class="scripture__and">AND</span>
    <span class="scripture__they">THEY</span>
    <span class="scripture__prophesied">PROPHESIED</span>
    <span class="scripture__also">ALSO</span>
  </div>

  <div class="date date--november">
    <div class="date__month">NOVEMBER</div>
    <div class="date__day">2019.  29</div>
  </div>

  <p class="time"><span class="time__hour">6:30</span>PM-<span class="time__hour">9:00</span>PM</p>

  <p class="venue"><span class="venue__name">HOLLARD COMMUNITY CENTER</span> · 482 WENDLE STREET, PORTLAND, ME 04102</p>

  <p class="keywords">PROPHETIC<span class="keywords__sep">,</span> HEALING<span class="keywords__sep">,</span> CLIMBING IN THE SPIRIT</p>
  <p class="tagline">HIGHER LEVEL OF ANOINTING...</p>

  <svg class="divider" viewBox="0 0 636 6" aria-hidden="true">
    <line x1="3" y1="3" x2="633" y2="3" stroke="#f7931e" stroke-width="4" stroke-linecap="round" stroke-dasharray="0 9"/>
  </svg>

  <div class="brand">
    <span class="brand__dot"></span>
    <span class="brand__name">TOVIK</span>
  </div>

  <div class="contact">
    <p class="contact__lead">FOR MORE INFO CALL US NOW</p>
    <p class="contact__phone">TEL. 207-555-3841</p>
    <p class="contact__row contact__row--email">
      <svg class="contact__icon" viewBox="0 0 30 22" aria-hidden="true">
        <rect x="1" y="1" width="28" height="20" fill="none" stroke="#ffffff" stroke-width="2"/>
        <polyline points="1,1 15,12 29,1" fill="none" stroke="#ffffff" stroke-width="2"/>
      </svg>
      CONTACT@BRIMFIELD-HALL.ORG
    </p>
    <p class="contact__row contact__row--web">
      <svg class="contact__icon contact__icon--globe" viewBox="0 0 28 28" aria-hidden="true">
        <circle cx="14" cy="14" r="12" fill="none" stroke="#ffffff" stroke-width="2"/>
        <ellipse cx="14" cy="14" rx="5" ry="12" fill="none" stroke="#ffffff" stroke-width="2"/>
        <line x1="2" y1="14" x2="26" y2="14" stroke="#ffffff" stroke-width="2"/>
        <line x1="4" y1="8" x2="24" y2="8" stroke="#ffffff" stroke-width="1.5"/>
        <line x1="4" y1="20" x2="24" y2="20" stroke="#ffffff" stroke-width="1.5"/>
      </svg>
      WWW.TOVIK.ORG
    </p>
  </div>
</main>
</body>
</html>
```